Casa Soleta Deli

This customer just brought a deli that is failing around me. Saw his business card and thought he needed and upgrade on them. I tasted there food and it was great! The Deli mostly sells sandwiches and hot Spanish Foods. The deli is close the beach at least 10 minutes away. So beach colors should be the theme. Please be creative

Target Market(s)

blue collar market business next to a train station

Industry/Entity Type

Food Store

Contact Information for Business Card

all the information is on the the attachment you can change the design of the card. make sure you put Hispanic foods under casa soleta deli. Be creative

Colors

Designer to choose colors to be used in the design.

Requirements
Must have
• food picture one full chicken and a Cuban-sandwich.

```html
<!DOCTYPE html>
<html lang="en">
<head>
<meta charset="UTF-8">
<title>Casa Soleta Deli – Business Card</title>
<link href="https://fonts.googleapis.com/css2?family=Exo+2:wght@400;600;800&family=Quicksand:wght@400&display=swap" rel="stylesheet">
<style>
  :root {
    --bg: #e9e4dc;
    --orange-light: #f3a032;
    --orange: #e27a1e;
    --orange-deep: #b8470f;
    --ink: #111111;
    --gold: #f2b51c;
    --white: #ffffff;
    --photo-chicken: #c9803a;
    --photo-bread: #c98d4e;
    --photo-roast: #b5531c;
    --photo-cuban: #d7b070;
  }
  * { margin: 0; padding: 0; box-sizing: border-box; }
  html, body { width: 1200px; height: 780px; overflow: hidden; }
  body {
    background: var(--bg);
    display: flex;
    align-items: center;
    justify-content: center;
    font-family: "Exo 2", sans-serif;
  }
  .card {
    position: relative;
    width: 1000px;
    height: 572px;
    background: var(--ink);
    overflow: hidden;
    box-shadow: 0 10px 30px rgba(0,0,0,.25);
  }
  .card__header {
    position: absolute;
    left: 0; top: 0;
    width: 100%; height: 250px;
    background: linear-gradient(100deg, var(--orange-deep) 0%, var(--orange) 45%, var(--orange-light) 100%);
    padding: 0 56px;
    display: flex;
    align-items: center;
    justify-content: space-between;
  }
  .brand__name {
    font-weight: 800;
    font-size: 66px;
    line-height: 1;
    color: var(--ink);
    letter-spacing: 1px;
  }
  .brand__tagline {
    font-family: "Quicksand", sans-serif;
    font-size: 30px;
    letter-spacing: 11px;
    color: var(--ink);
    margin-top: 10px;
    margin-left: 4px;
  }
  .contact-person { text-align: left; align-self: flex-start; margin-top: 44px; }
  .contact-person__name {
    font-weight: 800;
    font-size: 46px;
    color: var(--ink);
    line-height: 1;
  }
  .contact-person__phone {
    display: flex;
    align-items: center;
    gap: 10px;
    font-weight: 800;
    font-size: 30px;
    color: var(--ink);
    margin-top: 10px;
  }
  .contact-person__phone svg { width: 28px; height: 28px; }
  .divider {
    position: absolute;
    left: 0; width: 100%;
    height: 14px;
    background: var(--ink);
    border-top: 3px solid var(--gold);
  }
  .divider--top { top: 250px; border-top: none; border-bottom: 4px solid var(--gold); }
  .photo-strip {
    position: absolute;
    left: 0; top: 264px;
    width: 100%; height: 196px;
    display: grid;
    grid-template-columns: 1fr 1fr 1fr 1fr;
    gap: 6px;
    background: var(--ink);
  }
  .photo { width: 100%; height: 100%; }
  .photo--chicken-plate { background: radial-gradient(circle at 50% 55%, var(--photo-chicken), #f1e6d4 80%); }
  .photo--sandwich { background: linear-gradient(135deg, var(--photo-bread), #efe0c0); }
  .photo--roast-chicken { background: radial-gradient(circle at 50% 50%, var(--photo-roast), #5a200a); }
  .photo--cuban-sandwich { background: linear-gradient(135deg, #f3dca0, var(--photo-cuban) 50%, #a2473a); }
  .card__footer {
    position: absolute;
    left: 0; top: 460px;
    width: 100%; height: 112px;
    background: var(--ink);
    border-top: 4px solid var(--gold);
    display: flex;
    align-items: center;
    padding: 0 56px;
    gap: 18px;
    font-size: 28px;
    color: var(--gold);
  }
  .card__footer .label { font-weight: 800; }
  .card__footer .sep { font-weight: 400; }
</style>
</head>
<body>
  <article class="card">
    <header class="card__header">
      <div class="brand">
        <div class="brand__name">Casa Soleta Deli</div>
        <div class="brand__tagline">Hispanic foods</div>
      </div>
      <div class="contact-person">
        <div class="contact-person__name">Marco Ruiz</div>
        <div class="contact-person__phone">
          <svg viewBox="0 0 24 24" aria-hidden="true"><rect width="24" height="24" rx="4" fill="#111"/><path d="M7 4c1 0 2 3 2 4s-1 1-1 2 3 5 5 5 1-1 2-1 4 1 4 2-1 4-3 4C9 20 4 14 4 8c0-2 2-4 3-4z" fill="#fff"/></svg>
          <span>0198 765 432</span>
        </div>
      </div>
    </header>
    <div class="divider divider--top"></div>
    <section class="photo-strip">
      <div class="photo photo--chicken-plate" role="img" aria-label="Photo of a whole roast chicken on a plate with carrots"></div>
      <div class="photo photo--sandwich" role="img" aria-label="Photo of a toasted pressed sandwich"></div>
      <div class="photo photo--roast-chicken" role="img" aria-label="Photo of a glazed roast chicken close-up"></div>
      <div class="photo photo--cuban-sandwich" role="img" aria-label="Photo of a Cuban sandwich with ham and cheese"></div>
    </section>
    <footer class="card__footer">
      <span><span class="label">E:</span> hello@casasoleta.com</span>
      <span class="sep">|</span>
      <span><span class="label">W:</span> www.casasoletadeli.com</span>
    </footer>
  </article>
</body>
</html>
```